Business Card Design for Event Planning Company

Create a business card for event planning company using our new logo. After I pick the design, I will need files made for 6 employees. Our company provides event design & logistics services as well as venue management. The font should be sans serif and complementary to the logo. I will need to know the name of the font selected for the final design. The phone numbers listed should be separated by "." not "-"

Address for the card
PO Box 318, Washington, DC 20019

Card One
Lorna Pettibone
lpettibone@galavoyant.com
202.481.7730

Card Two
Miriam Okonkwo
mokonkwo@galavoyant.com
202.556.2047

Card Three
Tessa Varnholt
tvarnholt@galavoyant.com
978.620.4471

Card Four
Robin Fess
rfess@galavoyant.com
202.718.3362

Card Five
Ada-Rose Pelletan-Uzor
adarose@galavoyant.com
202.839.1205

Card Six
Beatrix Holloway
Beatrix@galavoyant.com
202.492.6618

Target Market(s)

Corporate/Non-Profit

Industry/Entity Type

Event Planning

Contact Information for Business Card

Address for the card

Card One
Lorna Pettibone
lpettibone@galavoyant.com
202.481.7730

Card Two
Miriam Okonkwo
202.556.2047

Card Three
Tessa Varnholt
978.620.4471

Card Four
Robin Fess
rfess@galavoyant.com
202.718.3362

Card Five
Ada-Rose Pelletan-Uzor
202.839.1205

Card Six
Beatrix Holloway
202.492.6618

Font styles to use
Sans Serif

Colors

Designer to choose colors to be used in the design.

Requirements
Must have
• Two-sided with logo
Should not have
• Extra colors or be too busy

```html
<!DOCTYPE html>
<html lang="en">
<head>
<meta charset="utf-8">
<title>Galavoyant — Business Card</title>
<link rel="stylesheet" href="https://fonts.googleapis.com/css2?family=Montserrat:wght@700&family=Questrial&display=swap">
<style>
  :root {
    --teal: #5ba8a6;
    --ink: #1b1b1b;
    --paper: #ffffff;
    --backdrop: #e9ebea;
    --shadow: rgba(0, 0, 0, 0.14);
  }
  * { box-sizing: border-box; margin: 0; padding: 0; }
  html, body {
    width: 1200px;
    height: 800px;
    overflow: hidden;
    background: var(--backdrop);
  }
  .stage {
    position: relative;
    width: 1200px;
    height: 800px;
  }
  .card {
    position: absolute;
    top: 85px;
    width: 360px;
    height: 630px;
    overflow: hidden;
    box-shadow: 0 10px 30px var(--shadow);
  }
  .card--front { left: 210px; background: var(--paper); }
  .card--back  { left: 630px; background: var(--teal); }

  .card__shapes {
    position: absolute;
    inset: 0;
    width: 100%;
    height: 100%;
  }

  .wordmark {
    position: absolute;
    left: 0;
    right: 0;
    display: flex;
    align-items: center;
    justify-content: center;
    gap: 10px;
    font-family: "Questrial", sans-serif;
    color: var(--ink);
    letter-spacing: 0.5px;
  }
  .wordmark__dot {
    width: 22px;
    height: 22px;
    border-radius: 50%;
    background: var(--ink);
  }
  .card--front .wordmark { top: 120px; font-size: 40px; }
  .card--back .wordmark  { top: 290px; font-size: 46px; }
  .card--back .wordmark__dot { width: 26px; height: 26px; }

  .contact {
    position: absolute;
    left: 0;
    right: 0;
    top: 350px;
    text-align: center;
    color: var(--paper);
    font-family: "Questrial", sans-serif;
  }
  .contact__name {
    font-family: "Montserrat", sans-serif;
    font-weight: 700;
    font-size: 21px;
    letter-spacing: 0.5px;
    text-transform: uppercase;
    margin-bottom: 26px;
  }
  .contact__line {
    font-size: 15px;
    line-height: 27px;
  }
</style>
</head>
<body>
<main class="stage">

  <section class="card card--front" aria-label="Card front">
    <svg class="card__shapes" viewBox="0 0 360 630" preserveAspectRatio="none" aria-hidden="true">
      <path class="swoosh" d="M0 232 C 110 222, 260 240, 360 300 L 360 318 C 260 254, 110 238, 0 246 Z" fill="var(--ink)"/>
      <path class="panel" d="M0 250 C 110 242, 260 258, 360 322 L 360 630 L 0 630 Z" fill="var(--teal)"/>
    </svg>

    <div class="wordmark">
      <span class="wordmark__dot"></span>
      <span class="wordmark__text">galavoyant</span>
    </div>

    <div class="contact">
      <p class="contact__name">Lorna Pettibone</p>
      <p class="contact__line">lpettibone@galavoyant.com</p>
      <p class="contact__line">202.481.7730</p>
      <p class="contact__line">PO Box 318, Washington, DC 20019</p>
    </div>
  </section>

  <section class="card card--back" aria-label="Card back">
    <div class="wordmark">
      <span class="wordmark__dot"></span>
      <span class="wordmark__text">galavoyant</span>
    </div>
  </section>

</main>
</body>
</html>
```